PDN Letterhead

We need a letterhead design that will be able to be used on all marketing products (letterhead, mail chimp, envelops, business cards, etc.) We are a law firm specializing primarily in transportation law but offer a wide range of services to our clients. We would like the design to be modern, simple, and professional. Our colors are black and gold, however, we've incorporated dark gray and white on other marketing products such as our website.

```html
<!DOCTYPE html>
<html lang="en">
<head>
<meta charset="utf-8">
<title>PDN Law Group Stationery</title>
<link rel="stylesheet" href="https://fonts.googleapis.com/css2?family=Open+Sans:wght@400;600;700&display=swap">
<style>
  :root {
    --gold: #b79d77;
    --black: #1b1b1c;
    --paper: #f1f1f0;
    --ink: #2a2a2a;
    --stage: #e6e3de;
  }
  * { margin: 0; padding: 0; box-sizing: border-box; }
  html, body { width: 1200px; height: 791px; overflow: hidden; }
  body {
    background: var(--stage);
    font-family: "Open Sans", Arial, sans-serif;
    color: var(--ink);
    position: relative;
  }
  .sheet {
    position: absolute;
    background: var(--paper);
    box-shadow: 0 6px 14px rgba(0,0,0,.18);
    overflow: hidden;
  }
  .sheet > svg.art { position: absolute; inset: 0; width: 100%; height: 100%; }
  .letterhead { left: 139px; top: 41px; width: 414px; height: 532px; }
  .envelope   { left: 669px; top: 137px; width: 450px; height: 198px; }
  .card-front { left: 664px; top: 434px; width: 203px; height: 122px; }
  .card-back  { left: 909px; top: 434px; width: 203px; height: 122px; }

  .brand { position: absolute; display: flex; align-items: center; gap: 6px; }
  .brand-mark { width: 9px; height: 9px; background: var(--gold); flex: none; }
  .brand-name {
    font-weight: 600; color: var(--black); letter-spacing: .06em;
    text-transform: uppercase; line-height: 1.05;
  }
  .brand-name span { display: block; }
  .letterhead .brand { left: 34px; top: 62px; }
  .letterhead .brand-name { font-size: 13px; }
  .envelope .brand { left: 32px; top: 76px; }
  .envelope .brand-name { font-size: 12px; }
  .card-front .brand { left: 22px; top: 42px; }
  .card-front .brand-name { font-size: 13px; }
  .card-back .brand { left: 12px; top: 44px; }
  .card-back .brand-name { font-size: 11px; color: #fff; }

  .contact { position: absolute; list-style: none; color: #333; }
  .contact li { display: flex; align-items: center; gap: 4px; white-space: nowrap; }
  .icon { width: 6px; height: 6px; fill: var(--gold); flex: none; }

  .letterhead .contact {
    left: 185px; top: 484px; font-size: 8px;
    display: grid; grid-template-columns: auto auto; column-gap: 8px; row-gap: 3px;
  }
  .envelope .contact { left: 32px; top: 123px; font-size: 7.5px; display: grid; row-gap: 2.5px; }

  .card-back .person { position: absolute; right: 11px; top: 31px; text-align: right; }
  .person-name { font-size: 9.5px; font-weight: 700; color: var(--black); line-height: 1.1; }
  .person-role { font-size: 5.5px; color: #333; }
  .card-back .contact { right: 0; top: 59px; font-size: 5.5px; display: grid; row-gap: 3px; }
  .card-back .contact li { justify-content: flex-end; }
  .card-back .contact .icon { fill: var(--black); width: 4px; height: 4px; }
  .card-back .contact li::after { content: ""; width: 9px; height: .6px; background: var(--black); }
</style>
</head>
<body>

<svg width="0" height="0" style="position:absolute" aria-hidden="true">
  <defs>
    <symbol id="i-phone" viewBox="0 0 10 10"><path d="M2 1l2 2-1 1.2c.6 1.3 1.5 2.2 2.8 2.8L7 6l2 2-1.3 1.5C4.5 9 1 5.5.5 2.3z"/></symbol>
    <symbol id="i-mail" viewBox="0 0 10 10"><rect x="0" y="2" width="10" height="6" rx="1"/></symbol>
    <symbol id="i-pin" viewBox="0 0 10 10"><path d="M5 0a3.5 3.5 0 0 1 3.5 3.5C8.5 6 5 10 5 10S1.5 6 1.5 3.5A3.5 3.5 0 0 1 5 0zm0 2a1.5 1.5 0 1 0 0 3 1.5 1.5 0 0 0 0-3z"/></symbol>
    <symbol id="i-web" viewBox="0 0 10 10"><circle cx="5" cy="5" r="4.5"/></symbol>
  </defs>
</svg>

<!-- Letterhead -->
<section class="sheet letterhead">
  <svg class="art" viewBox="0 0 414 532" preserveAspectRatio="none" aria-hidden="true">
    <polygon fill="var(--gold)" points="0,0 414,0 414,15 176,15 176,10 0,10"/>
    <polygon fill="var(--black)" points="0,10 176,10 180,15 414,15 414,50 272,50 252,30 0,30"/>
    <g fill="var(--gold)">
      <polygon points="380,50 414,18 414,24 386,50"/>
      <polygon points="392,50 414,30 414,36 398,50"/>
      <polygon points="404,50 414,41 414,47 410,50"/>
    </g>
    <polygon fill="var(--black)" points="0,500 9,492 143,492 163,512 414,512 414,532 0,532"/>
    <g fill="var(--gold)">
      <polygon points="0,492 20,492 0,511"/>
      <polygon points="26,492 34,492 0,523 0,516"/>
      <polygon points="40,492 48,492 4,532 0,532 0,528"/>
    </g>
  </svg>
  <div class="brand">
    <i class="brand-mark"></i>
    <p class="brand-name"><span>PDN</span><span>Law Group</span></p>
  </div>
  <ul class="contact">
    <li><svg class="icon"><use href="#i-phone"/></svg>+111 555 0148</li>
    <li><svg class="icon"><use href="#i-mail"/></svg>hello@pdnlaw.com</li>
    <li><svg class="icon"><use href="#i-pin"/></svg>Harbor Street, Leeds</li>
    <li><svg class="icon"><use href="#i-web"/></svg>www.pdnlaw.com</li>
  </ul>
</section>

<!-- Envelope -->
<section class="sheet envelope">
  <svg class="art" viewBox="0 0 450 198" preserveAspectRatio="none" aria-hidden="true">
    <polygon fill="var(--gold)" points="0,0 450,0 450,17 180,17 177,14 0,14"/>
    <polygon fill="var(--black)" points="0,14 177,14 180,17 450,17 450,51 278,51 258,33 0,33"/>
    <g fill="var(--gold)">
      <polygon points="411,51 450,19 450,25 418,51"/>
      <polygon points="424,51 450,30 450,36 431,51"/>
      <polygon points="437,51 450,41 450,47 444,51"/>
    </g>
  </svg>
  <div class="brand">
    <i class="brand-mark"></i>
    <p class="brand-name"><span>PDN</span><span>Law Group</span></p>
  </div>
  <ul class="contact">
    <li><svg class="icon"><use href="#i-mail"/></svg>hello@pdnlaw.com</li>
    <li><svg class="icon"><use href="#i-phone"/></svg>+111 555 0148</li>
    <li><svg class="icon"><use href="#i-pin"/></svg>Harbor Street, Leeds</li>
    <li><svg class="icon"><use href="#i-web"/></svg>www.pdnlaw.com</li>
  </ul>
</section>

<!-- Business card, front -->
<section class="sheet card-front">
  <svg class="art" viewBox="0 0 203 122" preserveAspectRatio="none" aria-hidden="true">
    <polygon fill="var(--gold)" points="186,0 194,0 154,80 146,88 124,122 122,122 141,84 146,70"/>
    <polygon fill="var(--black)" points="194,0 203,0 203,122 131,122 150,88 154,80"/>
  </svg>
  <div class="brand">
    <i class="brand-mark"></i>
    <p class="brand-name"><span>PDN</span><span>Law Group</span></p>
  </div>
</section>

<!-- Business card, back -->
<section class="sheet card-back" style="background:var(--black)">
  <svg class="art" viewBox="0 0 203 122" preserveAspectRatio="none" aria-hidden="true">
    <polygon fill="var(--paper)" points="127,0 138,0 82,122 64,122 76,96 80,92"/>
    <polygon fill="var(--gold)" points="138,0 203,0 203,122 72,122 88,92"/>
  </svg>
  <div class="brand">
    <i class="brand-mark"></i>
    <p class="brand-name"><span>PDN</span><span>Law Group</span></p>
  </div>
  <div class="person">
    <p class="person-name">Alan Reyes</p>
    <p class="person-role">Director</p>
  </div>
  <ul class="contact">
    <li>hello@pdnlaw.com<svg class="icon"><use href="#i-mail"/></svg></li>
    <li>+111 555 0148<svg class="icon"><use href="#i-phone"/></svg></li>
    <li>Harbor Street, Leeds<svg class="icon"><use href="#i-pin"/></svg></li>
    <li>www.pdnlaw.com<svg class="icon"><use href="#i-web"/></svg></li>
  </ul>
</section>

</body>
</html>
```